New Stationary for our business

We are a gift business and would like to create a new corporate image with new stationary and design.

We would like a Classic Corporate look with a touch of Flair.

We would need:
Envelopes
Letter Head
Business Cards
With Comp Slips
Note Pads
Etc...

Our details are:

Basket Haven Pty Ltd
518 Tallow Street, Fernmead, Victoria, 3071
1800 742 918
www.baskethaven-demo.com.au
sales@baskethaven-demo.com.au

ABN: 58 603 214 796

Target Market(s)

Corporate Look

Industry/Entity Type

Marketing

Contact Information for Business Card

Basket Haven Pty Ltd
1800 742 918
518 Tallow Street
Fernmead 3071
Victoria Australia

Darren Pelluso - Managing Director
darren.pelluso@baskethaven-demo.com.au
0413 587 120

Logo Text

Basket Haven - The Gift Specialists

Colors

Designer to choose colors to be used in the design.

Requirements
Must have
• Look and Feel upmarket and exclusive

```html
<!DOCTYPE html>
<html lang="en">
<head>
<meta charset="utf-8">
<title>Basket Haven Stationery</title>
<link href="https://fonts.googleapis.com/css2?family=Open+Sans:wght@400;600;800&family=Tinos&display=swap" rel="stylesheet">
<style>
  :root {
    --bg: #e3e3e3;
    --paper: #f7f7f7;
    --ink: #111111;
    --red: #ee4532;
    --orange: #f26f21;
    --rule: #9a9a9a;
    --text: #222222;
  }
  * { margin: 0; padding: 0; box-sizing: border-box; }
  html, body { width: 1200px; height: 673px; overflow: hidden; }
  body {
    background: var(--bg);
    font-family: "Open Sans", sans-serif;
    color: var(--text);
    position: relative;
  }
  .piece { position: absolute; background: var(--paper); }

  .brand { position: absolute; }
  .brand-name {
    display: flex; align-items: center; gap: 0.25em;
    font-family: "Open Sans", sans-serif; font-weight: 800;
    color: var(--ink); line-height: 1; white-space: nowrap;
  }
  .brand-dot { width: 0.4em; height: 0.4em; border-radius: 50%; background: var(--red); flex: none; }
  .brand.on-color .brand-name { color: #ffffff; }
  .brand.on-color .brand-dot { background: #ffffff; }

  .contact { list-style: none; font-size: 5.6px; line-height: 1.5; }
  .contact li { display: flex; align-items: flex-start; gap: 5px; white-space: nowrap; }
  .contact svg { width: 5px; height: 5px; flex: none; margin-top: 1.5px; fill: var(--red); }
  .company { font-family: "Tinos", serif; font-size: 6.4px; color: var(--ink); margin-bottom: 2px; }
  .company .accent { color: var(--red); }

  /* Hero logo */
  .hero { left: 466px; top: 108px; }
  .hero .brand-name { font-size: 44px; }

  /* Letterhead */
  .letterhead { left: 72px; top: 82px; width: 348px; height: 492px; }
  .letterhead .brand { left: 108px; top: 30px; }
  .letterhead .brand-name { font-size: 15px; }
  .letterhead .footer-rule { position: absolute; left: 12px; right: 24px; top: 441px; height: 1px; background: var(--rule); }
  .letterhead .footer-left { position: absolute; left: 18px; top: 450px; }
  .letterhead .footer-right { position: absolute; left: 230px; top: 450px; }

  /* Business cards */
  .card-front {
    left: 442px; top: 236px; width: 164px; height: 93px;
    background: linear-gradient(135deg, var(--red) 35%, var(--orange));
  }
  .card-front .brand { left: 30px; top: 38px; }
  .card-front .brand-name { font-size: 13.5px; }

  .card-back { left: 633px; top: 236px; width: 165px; height: 93px; }
  .card-back .brand { left: 10px; top: 13px; }
  .card-back .brand-name { font-size: 9.5px; }
  .card-back .name-line { position: absolute; left: 9px; right: 9px; top: 38px; height: 0.6px; background: #555; }
  .card-back .person { position: absolute; left: 92px; top: 33px; background: var(--paper); padding: 0 3px; }
  .card-back .person-name { font-size: 6.4px; color: var(--ink); line-height: 1; }
  .card-back .person-role { font-size: 2.8px; color: var(--red); letter-spacing: 0.08em; }
  .card-back .contact { font-size: 3.6px; }
  .card-back .contact svg { width: 3.4px; height: 3.4px; margin-top: 0.8px; }
  .card-back .col-left { position: absolute; left: 9px; top: 62px; }
  .card-back .col-right { position: absolute; left: 93px; top: 62px; }
  .card-back .bar, .envelope .bar { position: absolute; left: 0; right: 0; bottom: 0; background: linear-gradient(90deg, var(--red), var(--orange)); }
  .card-back .bar { height: 5px; }

  /* Envelope */
  .envelope { left: 443px; top: 352px; width: 361px; height: 220px; }
  .envelope .flap { position: absolute; left: 0; top: 0; width: 361px; height: 40px; }
  .envelope .flap .brand { left: 150px; top: 14px; transform: rotate(180deg); }
  .envelope .flap .brand-name { font-size: 9px; }
  .envelope .body-brand { left: 14px; top: 56px; }
  .envelope .body-brand .brand-name { font-size: 14px; }
  .envelope .contact { position: absolute; left: 14px; top: 169px; font-size: 4.5px; }
  .envelope .contact svg { width: 4px; height: 4px; margin-top: 1px; }
  .envelope .bar { height: 7px; }

  /* Notepad */
  .notepad { left: 835px; top: 172px; width: 285px; height: 403px; }
  .notepad .brand { left: 89px; top: 24px; }
  .notepad .brand-name { font-size: 14px; }
  .notepad .head-rule { position: absolute; left: 9px; right: 19px; top: 52px; height: 1.5px; background: var(--red); }
  .notepad .writing-lines {
    position: absolute; left: 9px; right: 19px; top: 54px; height: 304px;
    background: repeating-linear-gradient(to bottom, transparent 0, transparent 10.7px, #b9b9b9 10.7px, #b9b9b9 11.7px);
  }
  .notepad .contact { font-size: 4.6px; }
  .notepad .contact svg { width: 4px; height: 4px; margin-top: 1px; }
  .notepad .company { font-size: 5.3px; }
  .notepad .footer-left { position: absolute; left: 14px; top: 368px; }
  .notepad .footer-right { position: absolute; left: 191px; top: 367px; }
</style>
</head>
<body>

<svg width="0" height="0" style="position:absolute" aria-hidden="true">
  <symbol id="icon-pin" viewBox="0 0 10 10"><path d="M5 0a3.5 3.5 0 0 0-3.5 3.5C1.5 6 5 10 5 10s3.5-4 3.5-6.5A3.5 3.5 0 0 0 5 0zm0 5a1.4 1.4 0 1 1 0-2.8A1.4 1.4 0 0 1 5 5z"/></symbol>
  <symbol id="icon-phone" viewBox="0 0 10 10"><path d="M2 0.5l2 2-1 1.4c.6 1.3 1.7 2.4 3 3l1.4-1 2 2-1.2 1.6C4.5 9.3.7 5.5.5 1.7z"/></symbol>
  <symbol id="icon-web" viewBox="0 0 10 10"><path d="M5 0a5 5 0 1 0 0 10A5 5 0 0 0 5 0zm0 1.2c.6.6 1.1 1.8 1.2 3.2H3.8C3.9 3 4.4 1.8 5 1.2zM1.3 5.6h1.4c.1 1.2.4 2.2.8 2.9A3.9 3.9 0 0 1 1.3 5.6zm1.4-1.2H1.3a3.9 3.9 0 0 1 2.2-2.9c-.4.7-.7 1.700-.8 2.9zM5 8.8c-.6-.6-1.1-1.8-1.2-3.2h2.4C6.1 7 5.6 8.2 5 8.8zm1.5-.3c.4-.7.7-1.7.8-2.9h1.4a3.9 3.9 0 0 1-2.2 2.9zm.8-4.1c-.1-1.2-.4-2.2-.8-2.9a3.9 3.9 0 0 1 2.2 2.9z"/></symbol>
  <symbol id="icon-mail" viewBox="0 0 10 10"><path d="M0 3l5 3 5-3v6H0zM1 1h8l-4 2.5z"/></symbol>
</svg>

<div class="brand hero">
  <div class="brand-name"><span class="brand-dot"></span>Basket Haven</div>
</div>

<section class="piece letterhead">
  <div class="brand">
    <div class="brand-name"><span class="brand-dot"></span>Basket Haven</div>
  </div>
  <div class="footer-rule"></div>
  <div class="footer-left">
    <p class="company"><span class="accent">Basket Haven</span> Pty Ltd</p>
    <ul class="contact">
      <li><svg><use href="#icon-pin"/></svg>518 Tallow Street, Fernmead, Victoria, 3071</li>
      <li><svg><use href="#icon-phone"/></svg>1800 742 918</li>
    </ul>
  </div>
  <ul class="contact footer-right">
    <li><svg><use href="#icon-web"/></svg>www.baskethaven-demo.com.au</li>
    <li><svg><use href="#icon-mail"/></svg>sales@baskethaven-demo.com.au</li>
    <li><svg></svg>ABN: 58 603 214 796</li>
  </ul>
</section>

<section class="piece card-front">
  <div class="brand on-color">
    <div class="brand-name"><span class="brand-dot"></span>Basket Haven</div>
  </div>
</section>

<section class="piece card-back">
  <div class="brand">
    <div class="brand-name"><span class="brand-dot"></span>Basket Haven</div>
  </div>
  <div class="name-line"></div>
  <div class="person">
    <p class="person-name">Corin Vale</p>
    <p class="person-role">DIRECTOR</p>
  </div>
  <ul class="contact col-left">
    <li><svg><use href="#icon-pin"/></svg>518 Tallow Street,<br>Fernmead, Victoria, 3071</li>
    <li><svg><use href="#icon-phone"/></svg>1800 742 918</li>
  </ul>
  <ul class="contact col-right">
    <li><svg><use href="#icon-web"/></svg>www.baskethaven-demo.com.au</li>
    <li><svg><use href="#icon-mail"/></svg>sales@baskethaven-demo.com.au</li>
    <li><svg></svg>ABN: 58 603 214 796</li>
  </ul>
  <div class="bar"></div>
</section>

<section class="piece envelope">
  <div class="flap">
    <svg width="361" height="40" viewBox="0 0 361 40" aria-hidden="true">
      <defs><linearGradient id="flap-fill" x1="0" x2="1"><stop offset="0" stop-color="#ee4532"/><stop offset="1" stop-color="#ef4b30"/></linearGradient></defs>
      <path d="M12 0H349Q353 0 354 4L361 40H0L8 4Q9 0 12 0Z" fill="url(#flap-fill)"/>
    </svg>
    <div class="brand on-color">
      <div class="brand-name"><span class="brand-dot"></span>Basket Haven</div>
    </div>
  </div>
  <div class="brand body-brand">
    <div class="brand-name"><span class="brand-dot"></span>Basket Haven</div>
  </div>
  <ul class="contact">
    <li><svg><use href="#icon-pin"/></svg>518 Tallow Street, Fernmead,<br>Victoria, 3071</li>
    <li><svg><use href="#icon-phone"/></svg>1800 742 918</li>
    <li><svg><use href="#icon-web"/></svg>www.baskethaven-demo.com.au</li>
    <li><svg><use href="#icon-mail"/></svg>sales@baskethaven-demo.com.au</li>
  </ul>
  <div class="bar"></div>
</section>

<section class="piece notepad">
  <div class="brand">
    <div class="brand-name"><span class="brand-dot"></span>Basket Haven</div>
  </div>
  <div class="head-rule"></div>
  <div class="writing-lines"></div>
  <div class="footer-left">
    <p class="company"><span class="accent">Basket Haven</span> Pty Ltd</p>
    <ul class="contact">
      <li><svg><use href="#icon-pin"/></svg>518 Tallow Street, Fernmead, Victoria, 3071</li>
      <li><svg><use href="#icon-phone"/></svg>1800 742 918</li>
    </ul>
  </div>
  <ul class="contact footer-right">
    <li><svg><use href="#icon-web"/></svg>www.baskethaven-demo.com.au</li>
    <li><svg><use href="#icon-mail"/></svg>sales@baskethaven-demo.com.au</li>
    <li><svg></svg>ABN: 58 603 214 796</li>
  </ul>
</section>

</body>
</html>
```